Financial Service Company Need Business Card Design

This is a new startup company, first of its kind to offer this service. We facilitate the movement of deposit funds electronically between home buyers and real estate brokerages.Our customers are DOMIVANS®, real estate brokerages, and home buyers, we identify ourselves as a financial/technology company.
Not looking for anything too flashy. Just a clean design that shows the logo, contact info, etc. Company colors can be seen on attached logo, and 'coming soon page'
www.quorvanta.ca

```html
<!DOCTYPE html>
<html lang="en">
<head>
<meta charset="utf-8">
<title>Quorvanta business card</title>
<link rel="stylesheet" href="https://fonts.googleapis.com/css2?family=Open+Sans:wght@400;600;700&display=swap">
<style>
  :root {
    --backdrop: #c9ccd2;
    --card-dark-top: #7a7b80;
    --card-dark-bottom: #5f6065;
    --card-light: #ffffff;
    --brand-orange: #e8552a;
    --ink-grey: #55575c;
    --ink-white: #ffffff;
  }
  * { box-sizing: border-box; margin: 0; padding: 0; }
  html, body {
    width: 1200px; height: 1024px; overflow: hidden;
    background: var(--backdrop);
    font-family: "Open Sans", Arial, sans-serif;
  }
  .sheet {
    width: 1200px; height: 1024px;
    display: flex; flex-direction: column; align-items: center; justify-content: center;
    gap: 56px;
  }
  .card {
    width: 700px; height: 400px; position: relative;
    box-shadow: 0 6px 18px rgba(0,0,0,0.18);
  }
  /* Front side */
  .card--front {
    background: linear-gradient(135deg, var(--card-dark-top), var(--card-dark-bottom));
    color: var(--ink-white);
  }
  .brand {
    position: absolute; left: 0; right: 0; top: 150px;
    display: flex; align-items: center; justify-content: center; gap: 18px;
  }
  .brand__square {
    width: 34px; height: 34px; background: var(--brand-orange);
  }
  .brand__name {
    font-size: 62px; font-weight: 600; letter-spacing: -1px; line-height: 1;
    color: var(--ink-white);
  }
  .front__url {
    position: absolute; right: 120px; top: 262px;
    font-size: 17px; letter-spacing: 0.5px; color: var(--ink-white);
  }
  /* Back side */
  .card--back { background: var(--card-light); color: var(--ink-grey); }
  .back__brand {
    position: absolute; right: 46px; top: 44px;
    display: flex; align-items: center; gap: 12px;
  }
  .back__brand .brand__square { width: 22px; height: 22px; }
  .back__brand .brand__name { font-size: 40px; color: var(--ink-grey); }
  .contact {
    position: absolute; left: 46px; top: 48px;
    list-style: none; font-size: 17px; line-height: 26px; color: var(--ink-grey);
  }
  .contact li { display: flex; align-items: center; gap: 12px; }
  .contact svg { width: 14px; height: 14px; flex: none; }
  .person {
    position: absolute; left: 46px; bottom: 58px;
  }
  .person__name {
    font-size: 24px; font-weight: 700; color: var(--brand-orange); line-height: 1.1;
  }
  .person__title { font-size: 16px; color: var(--ink-grey); }
  .accent-bar {
    position: absolute; left: 0; bottom: 0; width: 150px; height: 26px;
    background: var(--brand-orange);
  }
</style>
</head>
<body>
<main class="sheet">
  <section class="card card--front" aria-label="Card front">
    <div class="brand">
      <span class="brand__square"></span>
      <span class="brand__name">Quorvanta</span>
    </div>
    <p class="front__url">www.quorvanta.ca</p>
  </section>

  <section class="card card--back" aria-label="Card back">
    <ul class="contact">
      <li>
        <svg viewBox="0 0 14 14" aria-hidden="true"><path d="M3 1l2.5 2.5-1.3 1.6a8 8 0 0 0 4.7 4.7l1.6-1.3L13 11l-1.6 2C6 13 1 8 1 2.6z" fill="var(--brand-orange)"/></svg>
        555.014.2270
      </li>
      <li>
        <svg viewBox="0 0 14 14" aria-hidden="true"><rect x="3.5" y="0.8" width="7" height="12.4" rx="1.2" fill="none" stroke="var(--brand-orange)" stroke-width="1.4"/><circle cx="7" cy="11" r="0.8" fill="var(--brand-orange)"/></svg>
        555.014.2271
      </li>
      <li>
        <svg viewBox="0 0 14 14" aria-hidden="true"><rect x="1" y="3" width="12" height="8.5" fill="var(--brand-orange)"/><path d="M1 3l6 5 6-5" fill="none" stroke="#fff" stroke-width="1.2"/></svg>
        info@quorvanta.ca
      </li>
      <li>
        <svg viewBox="0 0 14 14" aria-hidden="true"><circle cx="7" cy="7" r="6" fill="var(--brand-orange)"/><path d="M1 7h12M7 1c-2.5 3-2.5 9 0 12M7 1c2.5 3 2.5 9 0 12" fill="none" stroke="#fff" stroke-width="0.9"/></svg>
        www.quorvanta.ca
      </li>
    </ul>

    <div class="back__brand">
      <span class="brand__square"></span>
      <span class="brand__name">Quorvanta</span>
    </div>

    <div class="person">
      <p class="person__name">Maren Holt</p>
      <p class="person__title">President</p>
    </div>
    <span class="accent-bar"></span>
  </section>
</main>
</body>
</html>
```